Spring 2026 Deck Construction Direct Mail Flier

The logo files I will include were named "maple ridge fixers" by the digital artist. However, my company is called Maple Ridge Yardworks (That was not a typo. There is no space between "home" and "service") If you'd like to experiment with color modification of the logo to make it fit better with designs you come up with, please be my guest.

I need a 6"x12" flier design to market my deck construction business. The expected goal is to get phone calls and book appointments for the upcoming Spring 2026 construction season. The call to action being something along the lines of "Call now; Appointments are going fast!"

My target audience is upper middle class (annual household income $100,000 - $200,000) families of 3-5 in the capital region of New York state, US. Houses are most commonly either vinyl sided, or sometimes a combination of vinyl siding and brick. The ideal flier design will feature this type of house. Also most houses in my target area have nice lawns with mulched gardens as well.

I prefer designs with more sweeping, gradual curves than sharp square edges and corners, though some squares and corners are ok. I like designs with pallets consisting of blue, red, green, black, gray. I do not like purple, pink, yellow, or orange.

If it's possible and will fit, it would be nice to have images of pressure treated lumber, western cedar decking, and composite decking, so that customers understand I can provide any of the three. Also listing them out would be great.

I prefer designs that are more visual than text-based. On at least one side the dominant element should be a visual of a large composite or cedar deck. An image somewhere - wherever it can fit - of a small (10'x14' or so), basic deck of pressure treated lumber would be ideal as well so that potential clients know I will build those. Also I would like some element, on either side, that creates a sense of urgency by drawing the eye to text along the lines of "2026 appointments are filling fast. Book your free consultation today!"

Selling points:
- Veteran owned and operated
- Hometown feel
- Personal service
- Satisfaction guaranteed

I will use the Northfield Parcel Bureau's "Bright Lane Route Mailer" (BLRM) service to deliver these, so on either the front or back there should be a small amount of reserved space in the top right corner for the NFPB's required markings (see https://www.larkstonepromo.com/products/plumber-fixit-blrm-postcard?variant=17305529816 for an example of the amount of space required). It's ok if there is imagery there and it gets covered up by the NFPB markings, it just shouldn't be anything important. You do not have to include the NFPB markings themselves. My print guy will do that when I pass him this design.

A final note on this; I've mentioned Spring 2026 several times. But I do not want the design to be relevant only for Spring. I'd like to use the design throughout the year so please no hard references to Spring that will make the flier seem out of place in the fall.

Thank you very much. I appreciate your time.

```html
<!DOCTYPE html>
<html lang="en">
<head>
<meta charset="utf-8">
<title>Maple Ridge Yardworks – Deck Construction Flier</title>
<link rel="stylesheet" href="https://fonts.googleapis.com/css2?family=Lato:ital,wght@0,400;0,700;0,900;1,400;1,700&display=swap">
<style>
  :root {
    --navy: #14305e;
    --red: #b3182a;
    --white: #ffffff;
    --backdrop: #d9dcdf;
    --gold: #c9a44a;
    --ink: #1b2a44;
  }
  * { box-sizing: border-box; margin: 0; padding: 0; }
  html, body { width: 1200px; height: 474px; overflow: hidden; }
  body {
    background: var(--backdrop);
    font-family: "Lato", Arial, sans-serif;
    position: relative;
  }
  .flier {
    position: absolute;
    top: 27px;
    width: 210px;
    height: 420px;
    background: var(--white);
    overflow: hidden;
    box-shadow: 0 2px 8px rgba(0,0,0,0.18);
  }
  .flier--front { left: 378px; }
  .flier--back { left: 612px; }
  .flier__art { position: absolute; inset: 0; width: 210px; height: 420px; }

  .brand-seal {
    position: absolute; left: 13px; top: 118px; width: 68px; height: 68px;
    border-radius: 50%; border: 2px solid var(--navy); background: var(--white);
    display: flex; align-items: center; justify-content: center; text-align: center;
  }
  .brand-seal__name {
    color: var(--navy); font-weight: 900; font-size: 8.5px; line-height: 1.1;
    text-transform: uppercase;
  }

  .headline {
    position: absolute; left: 14px; top: 205px;
    font-weight: 900; font-size: 22px; line-height: 20.5px; letter-spacing: -0.2px;
  }
  .headline__navy { color: var(--navy); display: block; }
  .headline__red { color: var(--red); display: block; }

  .urgency {
    position: absolute; left: 13px; top: 308px; color: var(--white);
    font-size: 11.5px; line-height: 13px;
  }
  .urgency strong { font-weight: 900; display: block; }
  .urgency span { font-weight: 400; display: block; margin-top: 1px; }

  .call-line {
    position: absolute; left: 13px; top: 377px; display: flex; align-items: center; gap: 8px;
  }
  .call-line__icon { width: 22px; height: 22px; }
  .call-line__number {
    color: var(--navy); font-weight: 900; font-size: 21px; letter-spacing: 0.2px;
  }

  .material-label {
    position: absolute; color: var(--navy); font-weight: 900; font-size: 6.8px;
    line-height: 7.4px; text-transform: uppercase;
  }
  .material-label--lumber { left: 13px; top: 96px; }
  .material-label--composite { right: 13px; top: 96px; text-align: right; }
  .material-label--cedar { left: 0; width: 210px; top: 209px; text-align: center; }

  .why {
    position: absolute; left: 13px; top: 237px;
  }
  .why__title { color: var(--red); font-weight: 900; font-size: 18px; line-height: 18px; }
  .why__company { color: var(--white); font-weight: 700; font-size: 7.6px; margin-top: 2px; }

  .selling-points {
    position: absolute; left: 13px; top: 284px; list-style: none;
  }
  .selling-points li {
    display: flex; align-items: center; gap: 5px;
    color: var(--white); font-size: 8.2px; line-height: 12px;
  }
  .selling-points svg { width: 8px; height: 8px; flex: none; }

  .ribbon-main {
    position: absolute; left: 0; width: 210px; top: 342px; line-height: 11px; text-align: center;
    color: var(--white); font-weight: 900; font-style: italic; font-size: 7.8px;
  }
  .ribbon-sub {
    position: absolute; left: 0; width: 210px; top: 360px; line-height: 11px; text-align: center;
    color: var(--white); font-style: italic; font-size: 6.6px;
  }
  .flier--back .call-line { top: 380px; }
</style>
</head>
<body>

<section class="flier flier--front" aria-label="Flier front">
  <svg class="flier__art" viewBox="0 0 210 420">
    <defs>
      <linearGradient id="yardTone" x1="0" y1="0" x2="0" y2="1">
        <stop offset="0" stop-color="#3f6b37"/>
        <stop offset="0.55" stop-color="#8a7a5f"/>
        <stop offset="1" stop-color="#4f7a35"/>
      </linearGradient>
      <linearGradient id="houseTone" x1="0" y1="0" x2="0" y2="1">
        <stop offset="0" stop-color="#8d7865"/>
        <stop offset="0.55" stop-color="#b59f86"/>
        <stop offset="0.85" stop-color="#c8b79e"/>
        <stop offset="1" stop-color="#5c8a3c"/>
      </linearGradient>
    </defs>
    <g role="img" aria-label="Photo: backyard deck with outdoor sofa, hedge and lawn">
      <path d="M0 0 H210 V128 C165 140 105 98 0 92 Z" fill="url(#yardTone)"/>
    </g>
    <path d="M0 92 C80 96 140 132 210 128 V140 C140 146 80 110 0 112 Z" fill="var(--navy)"/>
    <path d="M0 112 C80 110 140 146 210 140 V146 C140 154 80 118 0 118 Z" fill="var(--red)"/>
    <g role="img" aria-label="Photo: stone and siding house with large composite deck, patio table and umbrella">
      <path d="M210 150 V372 H150 C110 350 92 300 94 250 C96 190 140 152 210 150 Z" fill="url(#houseTone)"/>
    </g>
    <path d="M0 300 H138 C150 300 154 312 148 322 C140 338 152 356 182 360 L210 362 V372 H0 Z" fill="var(--red)"/>
    <path d="M150 340 C165 356 190 356 210 340 V372 H150 Z" fill="var(--navy)"/>
    <path d="M146 334 C160 352 188 354 210 334 V342 C190 360 162 360 150 342 Z" fill="var(--white)"/>
    <rect x="0" y="372" width="210" height="44" fill="var(--white)"/>
    <rect x="0" y="416" width="41" height="4" fill="var(--navy)"/>
    <rect x="41" y="416" width="169" height="4" fill="var(--red)"/>
    <circle cx="168" cy="91" r="28" fill="var(--gold)"/>
    <circle cx="168" cy="91" r="23" fill="var(--red)"/>
  </svg>

  <div class="brand-seal"><span class="brand-seal__name">Maple Ridge<br>Yardworks</span></div>

  <h1 class="headline">
    <span class="headline__navy">Build the</span>
    <span class="headline__navy">Deck Your</span>
    <span class="headline__red">Home</span>
    <span class="headline__red">Deserves</span>
  </h1>

  <p class="urgency">
    <strong>2026 appointments<br>are filling fast.</strong>
    <span>Book your free<br>consultation today!</span>
  </p>

  <div class="call-line">
    <svg class="call-line__icon" viewBox="0 0 24 24" aria-hidden="true">
      <path d="M6.5 2.5 L9.5 6.5 L7.5 9 C8.8 12 11.5 14.8 15 16.5 L17.5 14.5 L21.5 17.5 L19 21.5 C11 21 3 13 2.5 5 Z" fill="none" stroke="var(--red)" stroke-width="2" stroke-linejoin="round"/>
      <path d="M20 3 L14 9 M14 5 V9 H18" fill="none" stroke="var(--navy)" stroke-width="2" stroke-linecap="round"/>
    </svg>
    <span class="call-line__number">(518) 555-0147</span>
  </div>
</section>

<section class="flier flier--back" aria-label="Flier back">
  <svg class="flier__art" viewBox="0 0 210 420">
    <defs>
      <linearGradient id="fadeYard" x1="0" y1="0" x2="1" y2="0">
        <stop offset="0" stop-color="#4d7a3c"/>
        <stop offset="0.5" stop-color="#7e8a66"/>
        <stop offset="1" stop-color="#ffffff"/>
      </linearGradient>
      <linearGradient id="ptTone" x1="0" y1="0" x2="0" y2="1">
        <stop offset="0" stop-color="#6f9a55"/>
        <stop offset="1" stop-color="#a2553f"/>
      </linearGradient>
      <linearGradient id="cedarTone" x1="0" y1="0" x2="0" y2="1">
        <stop offset="0" stop-color="#5c8a3f"/>
        <stop offset="1" stop-color="#8a5a3a"/>
      </linearGradient>
      <linearGradient id="compositeTone" x1="0" y1="0" x2="0" y2="1">
        <stop offset="0" stop-color="#3f5f3a"/>
        <stop offset="1" stop-color="#8b9098"/>
      </linearGradient>
    </defs>
    <g role="img" aria-label="Photo: backyard patio seating fading into white">
      <rect x="0" y="0" width="145" height="92" fill="url(#fadeYard)"/>
    </g>
    <g role="img" aria-label="Photo: small pressure treated lumber deck with white table and chairs">
      <path d="M0 119 H66 Q73 119 73 126 V181 H0 Z" fill="url(#ptTone)"/>
    </g>
    <g role="img" aria-label="Photo: composite deck with table and planters">
      <path d="M144 119 H210 V181 H137 V126 Q137 119 144 119 Z" fill="url(#compositeTone)"/>
    </g>
    <g role="img" aria-label="Photo: western cedar deck with picnic table and trees">
      <rect x="66" y="135" width="78" height="65" rx="7" fill="url(#cedarTone)" stroke="var(--white)" stroke-width="2"/>
    </g>
    <path d="M0 283 V238 C40 222 90 222 130 232 C160 240 185 242 210 232 V372 H0 Z" fill="var(--navy)"/>
    <path d="M130 232 C160 240 185 242 210 232 V262 C185 262 160 252 130 232 Z" fill="var(--red)"/>
    <path d="M0 354 C60 344 150 344 210 354 V416 H0 Z" fill="var(--white)"/>
    <path d="M4 339 L206 335 L202 348 L206 357 L8 358 L12 349 Z" fill="var(--red)"/>
    <path d="M22 358 H188 L183 366 L188 374 H22 L27 366 Z" fill="var(--navy)"/>
    <rect x="0" y="416" width="41" height="4" fill="var(--navy)"/>
    <rect x="41" y="416" width="169" height="4" fill="var(--red)"/>
  </svg>

  <p class="material-label material-label--lumber">Pressure<br>Treated Lumber</p>
  <p class="material-label material-label--composite">Composite<br>Decking</p>
  <p class="material-label material-label--cedar">Western Cedar<br>Decking</p>

  <div class="why">
    <h2 class="why__title">Why Choose</h2>
    <p class="why__company">Maple Ridge Yardworks</p>
  </div>

  <ul class="selling-points">
    <li><svg viewBox="0 0 10 10" aria-hidden="true"><path d="M1 5 L4 8 L9 1" fill="none" stroke="var(--red)" stroke-width="2"/></svg>Veteran owned and operated</li>
    <li><svg viewBox="0 0 10 10" aria-hidden="true"><path d="M1 5 L4 8 L9 1" fill="none" stroke="var(--red)" stroke-width="2"/></svg>Hometown feel</li>
    <li><svg viewBox="0 0 10 10" aria-hidden="true"><path d="M1 5 L4 8 L9 1" fill="none" stroke="var(--red)" stroke-width="2"/></svg>Personal service</li>
    <li><svg viewBox="0 0 10 10" aria-hidden="true"><path d="M1 5 L4 8 L9 1" fill="none" stroke="var(--red)" stroke-width="2"/></svg>Satisfaction guaranteed</li>
  </ul>

  <p class="ribbon-main">Free On-Site Consultations Now Booking</p>
  <p class="ribbon-sub">Call Today Before Our Schedule Fills Up</p>

  <div class="call-line">
    <svg class="call-line__icon" viewBox="0 0 24 24" aria-hidden="true">
      <path d="M6.5 2.5 L9.5 6.5 L7.5 9 C8.8 12 11.5 14.8 15 16.5 L17.5 14.5 L21.5 17.5 L19 21.5 C11 21 3 13 2.5 5 Z" fill="none" stroke="var(--red)" stroke-width="2" stroke-linejoin="round"/>
      <path d="M20 3 L14 9 M14 5 V9 H18" fill="none" stroke="var(--navy)" stroke-width="2" stroke-linecap="round"/>
    </svg>
    <span class="call-line__number">(518) 555-0147</span>
  </div>
</section>

</body>
</html>
```